Business Card for boutique psychology business

Business card for boutique psychology practice in Melbourne. I want them to be relatively simply with the logo and backing colour taking up the front side. Then, text on the back, with my name; professional title (Clinical Psychologist); website - mirotherapy.com.au; email: hello@mirotherapy.com.au; insta: @miro.therapy.emdr
Back should also have the words: Attune. Restore. Flourish
Fonts used for logo are: Mikea Demo and Gotham Medium. Use something for back text that will compliment these.
Brand colours uploaded below. I'd like to see options in both olive and blush.

```html
<!DOCTYPE html>
<html lang="en">
<head>
<meta charset="utf-8">
<title>nerin therapy + EMDR — Business Cards</title>
<link href="https://fonts.googleapis.com/css2?family=Montserrat:wght@400;500&family=Cormorant+Garamond:ital,wght@1,400&display=swap" rel="stylesheet">
<style>
  :root {
    --backdrop: #e7e7e6;
    --olive: #4b5236;
    --olive-ink: #3f4530;
    --blush: #f3d9cf;
    --blush-ink: #ecd1c4;
    --paper: #f6f5f3;
    --title: #d79f86;
    --terracotta: #b7664f;
    --rule-white: #d8a897;
    --rule-blush: #c9a090;
    --tagline-blush: #5d5442;
  }
  * { margin: 0; padding: 0; box-sizing: border-box; }
  html, body { width: 1200px; height: 800px; overflow: hidden; }
  body { background: var(--backdrop); position: relative; font-family: "Montserrat", sans-serif; }

  .card { position: absolute; width: 456px; height: 263px; }
  .card--front { background: var(--olive); color: var(--blush-ink); }
  .card--back-white { background: var(--paper); }
  .card--back-blush { background: var(--blush); }

  .pos-tl { left: 121px; top: 101px; }
  .pos-tr { left: 623px; top: 101px; }
  .pos-bl { left: 121px; top: 435px; height: 264px; }
  .pos-br { left: 623px; top: 435px; height: 264px; }

  .brand { position: absolute; left: 0; right: 0; text-align: center; color: var(--blush-ink); }
  .brand__name { display: block; font-size: 86px; font-weight: 400; line-height: 1; letter-spacing: -1px; }
  .brand__sub { display: block; font-size: 20px; font-weight: 500; line-height: 1.2; margin-top: 4px; letter-spacing: 0.3px; }
  .pos-tl .brand { top: 66px; }
  .pos-bl .brand { top: 38px; }

  .front-tagline {
    position: absolute; left: 0; right: 0; top: 176px; text-align: center;
    font-family: "Cormorant Garamond", serif; font-style: italic; font-size: 22px;
    color: var(--blush-ink); letter-spacing: 0.5px;
  }

  .person { position: absolute; left: 31px; top: 30px; }
  .person__name { font-size: 26px; font-weight: 400; color: var(--olive-ink); line-height: 1.2; letter-spacing: 0.2px; }
  .person__title { font-size: 17px; font-weight: 400; color: var(--title); margin-top: 3px; letter-spacing: 0.2px; }

  .contacts { position: absolute; left: 31px; top: 112px; list-style: none; }
  .contacts li { display: flex; align-items: center; height: 30px; font-size: 16.5px; color: var(--olive-ink); letter-spacing: 0.2px; }
  .contacts svg { width: 16px; height: 16px; margin-right: 9px; flex: none; }

  .tagline-row {
    position: absolute; left: 31px; right: 46px; top: 208px;
    display: flex; align-items: center; gap: 10px;
  }
  .pos-br .tagline-row { top: 214px; }
  .tagline-row__rule { flex: 1; height: 1px; }
  .tagline-row__text { font-family: "Cormorant Garamond", serif; font-style: italic; font-size: 21px; letter-spacing: 0.5px; white-space: nowrap; }
  .card--back-white .tagline-row__rule { background: var(--rule-white); }
  .card--back-white .tagline-row__text { color: var(--terracotta); }
  .card--back-blush .tagline-row__rule { background: var(--rule-blush); }
  .card--back-blush .tagline-row__text { color: var(--tagline-blush); }
</style>
</head>
<body>

  <section class="card card--front pos-tl" aria-label="Card front, olive">
    <div class="brand">
      <span class="brand__name">nerin</span>
      <span class="brand__sub">therapy + EMDR</span>
    </div>
  </section>

  <section class="card card--back-white pos-tr" aria-label="Card back, white">
    <div class="person">
      <p class="person__name">Hannah Reid</p>
      <p class="person__title">Clinical Psychologist</p>
    </div>
    <ul class="contacts">
      <li>
        <svg viewBox="0 0 16 16" fill="none" stroke="#3f4530" stroke-width="1.3"><circle cx="8" cy="8" r="6.8"/><ellipse cx="8" cy="8" rx="3" ry="6.8"/><line x1="1.2" y1="8" x2="14.8" y2="8"/><line x1="2.4" y1="4.6" x2="13.6" y2="4.6"/><line x1="2.4" y1="11.4" x2="13.6" y2="11.4"/></svg>
        mirotherapy.com.au
      </li>
      <li>
        <svg viewBox="0 0 16 16"><rect x="1" y="2" width="14" height="12" rx="1.5" fill="#3f4530"/><path d="M4 6.5 L8 9.5 L12 6.5" fill="none" stroke="#f6f5f3" stroke-width="1.3"/></svg>
        hello@mirotherapy.com.au
      </li>
      <li>
        <svg viewBox="0 0 16 16"><rect x="1.5" y="1.5" width="13" height="13" rx="3" fill="none" stroke="#3f4530" stroke-width="1.5"/></svg>
        @miro.therapy.emdr
      </li>
    </ul>
    <div class="tagline-row">
      <span class="tagline-row__rule"></span>
      <span class="tagline-row__text">Attune. Restore. Flourish</span>
      <span class="tagline-row__rule"></span>
    </div>
  </section>

  <section class="card card--front pos-bl" aria-label="Card front, olive with tagline">
    <div class="brand">
      <span class="brand__name">nerin</span>
      <span class="brand__sub">therapy + EMDR</span>
    </div>
    <p class="front-tagline">Attune. Restore. Flourish</p>
  </section>

  <section class="card card--back-blush pos-br" aria-label="Card back, blush">
    <div class="person">
      <p class="person__name">Hannah Reid</p>
      <p class="person__title">Clinical Psychologist</p>
    </div>
    <ul class="contacts">
      <li>
        <svg viewBox="0 0 16 16" fill="none" stroke="#3f4530" stroke-width="1.3"><circle cx="8" cy="8" r="6.8"/><ellipse cx="8" cy="8" rx="3" ry="6.8"/><line x1="1.2" y1="8" x2="14.8" y2="8"/><line x1="2.4" y1="4.6" x2="13.6" y2="4.6"/><line x1="2.4" y1="11.4" x2="13.6" y2="11.4"/></svg>
        mirotherapy.com.au
      </li>
      <li>
        <svg viewBox="0 0 16 16"><rect x="1" y="2" width="14" height="12" rx="1.5" fill="#3f4530"/><path d="M4 6.5 L8 9.5 L12 6.5" fill="none" stroke="#f3d9cf" stroke-width="1.3"/></svg>
        hello@mirotherapy.com.au
      </li>
      <li>
        <svg viewBox="0 0 16 16"><rect x="1.5" y="1.5" width="13" height="13" rx="3" fill="none" stroke="#3f4530" stroke-width="1.5"/></svg>
        @miro.therapy.emdr
      </li>
    </ul>
    <div class="tagline-row">
      <span class="tagline-row__rule"></span>
      <span class="tagline-row__text">Attune. Restore. Flourish</span>
      <span class="tagline-row__rule"></span>
    </div>
  </section>

</body>
</html>
```